International online gaming platform needs a game UI design

1. We need a game interface for three kinds of theme based on our guideline and sample mockup.
2. The product type is the online casino games related, we need a series of casino games UIs, however, we can start on the game lobby first.
3. Three theme you might choose from or refer to:
A. 3D look & feel
B. Realistic casino theme
C. Richness and grandeur
D. European casino style
4. NOT ALLOWED to change the design layout.
MUST follow our sample mock up and ONLY redefine the design style.
5. All items must be in a stand-alone component, eg. Button, Tab, Icon,... etc.
6. We need the layout in vector shape, but we can review in JPG or PNG format.
7. The image size: 1366 x 768

Updated:
1. All items and their positions should be same as the sample UI we provided.
Please redesign all the items and create a new theme for it.
No need to create a new layout.
2. Although we accept the draft design, but all the items in UI should be completed.
3. All the wordings in the sample UI are confirmed, you might change the fonts.
4. For the avatar in the left hand side, you don't have to redraw it.
We already have our own avatar system implemented.
5. All the items such as icons, tabs, and buttons are free to redesign.

Dear designers,

We've increased our budget and raise the prize money to 800 USD.  
We also accept the draft design in PNG format and we can go through the details in handover stage.
Thank you very much. 

Reason: Dear designers, We decided to extend the deadline by 7 days. As mentioned in the task description, we are looking for a new style of design and you might refer to the below style. A. 3D look & feel B. Realistic casino theme C. Richness and grandeur D. European casino style If you are still interested in our project, please send us your work. Thank you very much!

Casino

```html
<!DOCTYPE html>
<html lang="en">
<head>
<meta charset="utf-8">
<title>Grand Tables Lobby</title>
<link rel="stylesheet" href="https://fonts.googleapis.com/css2?family=Russo+One&family=Roboto:wght@400;500;700&display=swap">
<style>
:root{
  --bg:#141414;
  --bg-deep:#0a0a0a;
  --silver-hi:#f2f2f2;
  --silver-mid:#bdbdbd;
  --silver-lo:#6e6e6e;
  --blue-hi:#3f6fd6;
  --blue:#1d3f9a;
  --blue-deep:#0f2466;
  --green-hi:#6fd04a;
  --green:#2f8f1f;
  --green-deep:#17550e;
  --gold-hi:#fff3a6;
  --gold:#f3c72a;
  --gold-deep:#b07a08;
  --lobby:#3b0b0b;
  --lobby-deep:#1a0303;
  --text:#ffffff;
  --text-dark:#1b1b1b;
  --accent-yellow:#ffe11a;
  --close:#d0241c;
}
*{box-sizing:border-box;margin:0;padding:0}
html,body{width:1200px;height:675px;overflow:hidden;background:var(--bg-deep)}
body{font-family:"Roboto",Arial,sans-serif;color:var(--text)}
.canvas{position:relative;width:1200px;height:675px;overflow:hidden;
  background:linear-gradient(180deg,#2a2a2a 0%,var(--bg) 40%,#0c0c0c 100%)}
.abs{position:absolute}

/* top bar */
.top-bar{left:0;top:0;width:1200px;height:35px;
  background:linear-gradient(180deg,#e8e8e8,#9a9a9a 55%,#6a6a6a)}
.brand{left:0;top:0;width:338px;height:35px;background:linear-gradient(180deg,#222,#000);
  display:flex;align-items:center;padding-left:18px;border-right:2px solid #555}
.brand-name{font-family:"Roboto",Arial,sans-serif;font-weight:700;font-size:24px;color:var(--gold);letter-spacing:1px}
.window-tools{left:1030px;top:4px;display:flex;gap:4px}
.tool{width:29px;height:28px;border-radius:3px;border:2px solid #5a7fd0;
  background:linear-gradient(180deg,#2c56b8,#0d1f5a);display:flex;align-items:center;justify-content:center}
.tool.close{background:linear-gradient(180deg,#ef4a3f,var(--close));border-color:#f08a84}

/* left column */
.clock{left:18px;top:44px;width:165px;height:26px;border-radius:5px;
  background:linear-gradient(180deg,#000,#2a2a2a);border:2px solid #555;
  font-size:10px;display:flex;align-items:center;justify-content:center}
.player-card{left:9px;top:77px;width:177px;height:274px;border-radius:8px;
  background:linear-gradient(180deg,var(--silver-hi),var(--silver-mid) 50%,var(--silver-lo))}
.avatar{left:14px;top:15px;width:149px;height:182px;
  background:linear-gradient(180deg,#3a3a3a,#111);border:1px solid #777}
.player-name{left:14px;top:197px;width:149px;height:25px;background:linear-gradient(180deg,#4a4a4a,#1e1e1e);
  font-size:15px;display:flex;align-items:center;justify-content:center}
.profile-btn{left:14px;top:226px;width:149px;height:38px;border-radius:3px;
  background:linear-gradient(180deg,var(--blue-hi),var(--blue) 60%,var(--blue-deep));
  display:flex;align-items:center;gap:18px;padding-left:8px;font-size:16px}
.profile-icon{width:28px;height:28px;background:#111;border:1px solid #444;display:flex;align-items:center;justify-content:center}
.menu-panel{left:9px;top:365px;width:177px;height:263px;border-radius:8px;
  background:linear-gradient(180deg,#d9d9d9,#a9a9a9 60%,#8a8a8a)}
.menu-btn{left:9px;width:155px;height:38px;border-radius:7px;border:2px solid #7f98d8;
  background:linear-gradient(180deg,#3c66c8,var(--blue) 55%,#0a1a52);
  display:flex;align-items:center;gap:10px;padding-left:6px;font-size:11.5px;box-shadow:0 2px 3px #0008}
.menu-icon{width:24px;height:24px;border-radius:3px;background:linear-gradient(180deg,#2f62c8,#0c2a77);
  border:1px solid #9db4ea;display:flex;align-items:center;justify-content:center}

/* game tabs */
.game-tab{top:44px;height:42px;border-radius:10px;border:2px solid #cfcfcf;
  font-family:"Russo One",sans-serif;font-size:19px;display:flex;align-items:center;justify-content:center;
  box-shadow:inset 0 2px 0 #ffffff66,0 2px 4px #000a}
.game-tab.active{background:linear-gradient(180deg,#5b84e0,var(--blue) 55%,var(--blue-deep))}
.game-tab.idle{background:linear-gradient(180deg,var(--green-hi),var(--green) 55%,var(--green-deep))}
.tab-icon{position:absolute;left:-4px;top:-6px;width:52px;height:46px;border-radius:50%}
.tab-icon.cards{background:radial-gradient(circle,#ffffff,#bbbbbb);border-radius:6px;transform:rotate(-8deg)}
.tab-icon.wheel{background:radial-gradient(circle,#d8b15a 0 20%,#7a1d12 22% 60%,#c93b23 62%);}
.tab-icon.dice{background:radial-gradient(circle,#666,#1c1c1c);width:40px;border-radius:8px}

/* dealer strip */
.dealer-feature{left:200px;top:90px;width:276px;height:133px;border-radius:6px;
  background:linear-gradient(180deg,#dcdcdc,#8a8a8a);padding:4px}
.dealer-feature-inner{width:100%;height:100%;background:linear-gradient(180deg,#0f2466,#08123a);border-radius:3px;position:relative}
.dealer-rail{left:490px;top:90px;width:703px;height:133px;border-radius:6px;
  background:linear-gradient(180deg,#e6e6e6,#9a9a9a);padding:5px}
.dealer-rail-inner{width:100%;height:100%;background:#0b0b0b;position:relative}
.dealer{position:absolute}
.dealer-photo{position:absolute;border-radius:6px;border:2px solid #2f8ad6;
  background:linear-gradient(180deg,#3b4b5c,#0b1116)}
.road-grid{position:absolute;background-color:#fff;
  background-image:linear-gradient(90deg,#6fa0d6 1px,transparent 1px),linear-gradient(180deg,#6fa0d6 1px,transparent 1px)}
.dealer-bar{position:absolute;display:flex;align-items:center;justify-content:space-between;
  background:#000;color:#fff}
.dealer-bar .deals{background:var(--blue);height:100%;display:flex;align-items:center;padding:0 8px}

/* filter bar */
.filter-bar{left:200px;top:227px;width:993px;height:42px;border-radius:4px;
  background:linear-gradient(180deg,#2a4fae,var(--blue-deep))}
.chip{position:absolute;top:4px;height:34px;border-radius:6px;
  background:linear-gradient(180deg,#f4f4f4,#bcbcbc 55%,#8f8f8f);color:var(--text-dark);
  display:flex;align-items:center;justify-content:center;font-size:13px;border:1px solid #555}
.search-field{position:absolute;left:160px;top:5px;width:285px;height:32px;border-radius:4px;
  background:linear-gradient(180deg,#cfcfcf,#a8a8a8);border:1px solid #666}
.filter-group{position:absolute;left:463px;top:4px;height:34px;display:flex;gap:2px}
.filter-group .chip{position:static;height:34px;border-radius:3px}
.filter-group .chip:first-child{border-radius:16px 3px 3px 16px}
.filter-group .chip:last-child{border-radius:3px 6px 6px 3px;gap:8px;font-size:15px}

/* lobby */
.lobby{left:200px;top:279px;width:993px;height:355px;border-radius:6px;
  background:radial-gradient(ellipse at 50% 40%,#5a1414,var(--lobby) 55%,var(--lobby-deep));
  border:2px solid #6b3a12;box-shadow:inset 0 0 0 2px #2a0505}
.scroll-track{left:968px;top:14px;width:12px;height:318px;background:#0a0a0a;border-radius:3px}
.scroll-thumb{left:-1px;top:8px;width:14px;height:30px;border-radius:3px;background:linear-gradient(90deg,#eee,#888)}
.table-card{position:absolute;width:307px;height:155px;border-radius:9px;border:2px solid var(--gold);
  background:linear-gradient(180deg,#101010,#000);box-shadow:0 0 0 2px #7a4b08,0 3px 6px #000}
.table-name,.table-fee{position:absolute;top:6px;font-size:12px;color:var(--accent-yellow)}
.table-name{left:13px}.table-fee{right:13px}
.table-limit,.table-seats{position:absolute;top:22px;font-size:12px;color:#fff}
.table-limit{left:13px}.table-seats{right:13px}
.join-coin{position:absolute;left:106px;top:14px;width:92px;height:55px;border-radius:50%;
  background:radial-gradient(ellipse at 40% 30%,var(--gold-hi),var(--gold) 45%,var(--gold-deep));
  border:2px solid #8a5a05;display:flex;align-items:center;justify-content:center;
  font-family:"Russo One",sans-serif;font-size:13px;color:#7a4a00}
.felt{position:absolute;left:6px;top:60px;width:292px;height:56px}
.seat-row{position:absolute;left:5px;bottom:5px;display:flex;gap:4px}
.seat{width:39px;height:29px;border-radius:3px;background:linear-gradient(180deg,#2a2a2a,#050505);
  border:1px solid #3a3a3a;display:flex;align-items:center;justify-content:center}
.seat.more{background:linear-gradient(180deg,var(--gold-hi),var(--gold) 50%,var(--gold-deep));border-color:#8a5a05}

/* bottom */
.bottom-bar{left:0;top:639px;width:1200px;height:36px;
  background:linear-gradient(180deg,#9a9a9a,#d9d9d9 40%,#7a7a7a)}
.balance{left:938px;top:642px;width:252px;height:31px;border-radius:10px;
  background:linear-gradient(180deg,#2a2a2a,#000);border:2px solid #666;display:flex;align-items:center}
.balance-label{width:88px;text-align:center;font-size:15px}
.currency{height:27px;width:48px;background:linear-gradient(180deg,var(--gold),var(--gold-deep));
  color:#000;font-size:9px;display:flex;align-items:center;justify-content:center;border:1px solid #000}
.balance-value{flex:1;text-align:center;font-size:14px}
.balance-end{width:14px;height:27px;background:linear-gradient(180deg,var(--gold),var(--gold-deep));border-radius:0 8px 8px 0}
</style>
</head>
<body>
<main class="canvas">

  <header class="abs top-bar"></header>
  <div class="abs brand"><span class="brand-name">GRAND TABLES</span></div>
  <nav class="abs window-tools" aria-label="Window tools">
    <span class="tool"><svg width="18" height="18" viewBox="0 0 18 18"><circle cx="7" cy="7" r="5" fill="none" stroke="#fff" stroke-width="2"/><path d="M11 11l5 5M4.5 7h5" stroke="#fff" stroke-width="2"/></svg></span>
    <span class="tool"><svg width="18" height="18" viewBox="0 0 18 18"><circle cx="7" cy="7" r="5" fill="none" stroke="#fff" stroke-width="2"/><path d="M11 11l5 5" stroke="#fff" stroke-width="2"/><text x="7" y="10" font-size="8" text-anchor="middle" fill="#fff">$</text></svg></span>
    <span class="tool"><svg width="18" height="18" viewBox="0 0 18 18"><path d="M6 14V3l9-2v11" fill="none" stroke="#fff" stroke-width="2"/><circle cx="4" cy="14" r="2.5" fill="#fff"/><circle cx="13" cy="12" r="2.5" fill="#fff"/></svg></span>
    <span class="tool"><svg width="18" height="18" viewBox="0 0 18 18" fill="none" stroke="#fff" stroke-width="2"><path d="M2 6V2h4M12 2h4v4M16 12v4h-4M6 16H2v-4"/></svg></span>
    <span class="tool close"><svg width="16" height="16" viewBox="0 0 16 16"><path d="M3 3l10 10M13 3L3 13" stroke="#fff" stroke-width="2.5"/></svg></span>
  </nav>

  <div class="abs clock">12/03/2014 &nbsp;09 : 18 AM</div>

  <section class="abs player-card">
    <div class="abs avatar" role="img" aria-label="Player avatar"></div>
    <div class="abs player-name">Xon125</div>
    <div class="abs profile-btn"><span class="profile-icon"><svg width="14" height="16" viewBox="0 0 14 16"><path d="M1 1h8l4 4v10H1z" fill="#fff"/></svg></span>Profile</div>
  </section>

  <nav class="abs menu-panel" aria-label="Help">
    <div class="abs menu-btn" style="top:15px"><span class="menu-icon"><svg width="14" height="14" viewBox="0 0 14 14" fill="none" stroke="#fff" stroke-width="2"><circle cx="2.5" cy="11.5" r="1.5" fill="#fff" stroke="none"/><path d="M1 6a7 7 0 0 1 7 7M1 1a12 12 0 0 1 12 12"/></svg></span>Announcements</div>
    <div class="abs menu-btn" style="top:62px"><span class="menu-icon"><svg width="14" height="14" viewBox="0 0 14 14"><rect x="5.5" y="1" width="3" height="8" fill="#fff"/><rect x="5.5" y="10.5" width="3" height="2.5" fill="#fff"/></svg></span>Rules &amp; Regulation</div>
    <div class="abs menu-btn" style="top:108px"><span class="menu-icon"><svg width="14" height="14" viewBox="0 0 14 14" fill="none" stroke="#fff" stroke-width="2"><circle cx="6" cy="6" r="4"/><path d="M9 9l4 4"/></svg></span>Quick tour</div>
  </nav>

  <nav aria-label="Games">
    <div class="abs game-tab active" style="left:200px;width:227px"><span class="tab-icon cards" role="img" aria-label="Playing cards"></span>Bacarat</div>
    <div class="abs game-tab idle" style="left:439px;width:233px"><span class="tab-icon cards" role="img" aria-label="Cards with six"></span>Super six</div>
    <div class="abs game-tab idle" style="left:678px;width:227px"><span class="tab-icon wheel" role="img" aria-label="Roulette wheel"></span>Roulette</div>
    <div class="abs game-tab idle" style="left:918px;width:228px"><span class="tab-icon dice" role="img" aria-label="Dice"></span>Sic Bo</div>
  </nav>

  <section class="abs dealer-feature">
    <div class="dealer-feature-inner">
      <div class="dealer-photo" style="left:6px;top:4px;width:88px;height:85px" role="img" aria-label="Dealer photo"></div>
      <div class="road-grid" style="left:95px;top:4px;width:168px;height:85px;background-size:10.5px 10.6px"></div>
      <div class="dealer-bar" style="left:6px;top:94px;width:257px;height:24px;font-size:11px;padding-left:8px;border-radius:4px;overflow:hidden">Dealer Name<span class="deals">Deals 999</span></div>
    </div>
  </section>

  <section class="abs dealer-rail">
    <div class="dealer-rail-inner">
      <div class="dealer" style="left:17px;top:15px;width:215px;height:90px">
        <div class="dealer-photo" style="left:0;top:0;width:66px;height:62px" role="img" aria-label="Dealer photo"></div>
        <div class="road-grid" style="left:68px;top:2px;width:147px;height:60px;background-size:9.2px 8.6px"></div>
        <div class="dealer-bar" style="left:0;top:64px;width:215px;height:16px;font-size:8px;padding-left:8px">Dealer Name<span class="deals">Deals 999</span></div>
      </div>
      <div class="dealer" style="left:243px;top:15px;width:215px;height:90px">
        <div class="dealer-photo" style="left:0;top:0;width:66px;height:62px" role="img" aria-label="Dealer photo"></div>
        <div class="road-grid" style="left:68px;top:2px;width:147px;height:60px;background-size:9.2px 8.6px"></div>
        <div class="dealer-bar" style="left:0;top:64px;width:215px;height:16px;font-size:8px;padding-left:8px">Dealer Name<span class="deals">Deals 999</span></div>
      </div>
      <div class="dealer" style="left:470px;top:15px;width:215px;height:90px">
        <div class="dealer-photo" style="left:0;top:0;width:66px;height:62px" role="img" aria-label="Dealer photo"></div>
        <div class="road-grid" style="left:68px;top:2px;width:147px;height:60px;background-size:9.2px 8.6px"></div>
        <div class="dealer-bar" style="left:0;top:64px;width:215px;height:16px;font-size:8px;padding-left:8px">Dealer Name<span class="deals">Deals 999</span></div>
      </div>
    </div>
  </section>

  <section class="abs filter-bar">
    <div class="chip" style="left:9px;width:150px;justify-content:flex-start;gap:14px;padding-left:6px;border-radius:6px 0 0 6px">
      <svg width="28" height="26" viewBox="0 0 28 26"><rect width="28" height="26" fill="#fff"/><circle cx="14" cy="9" r="5" fill="#111"/><path d="M5 25c0-7 4-10 9-10s9 3 9 10z" fill="#111"/></svg>Multiplayer</div>
    <div class="search-field"></div>
    <div class="filter-group">
      <span class="chip" style="width:114px">Join any</span>
      <span class="chip" style="width:47px">A&#8594;Z</span>
      <span class="chip" style="width:43px">$&#8595;</span>
      <span class="chip" style="width:47px">$&#8593;</span>
      <span class="chip" style="width:46px"><svg width="30" height="20" viewBox="0 0 30 20" fill="#111"><circle cx="9" cy="6" r="4"/><circle cx="21" cy="6" r="4"/><circle cx="15" cy="8" r="4.5"/><path d="M2 19c0-5 3-8 7-8s5 2 6 3c1-1 2-3 6-3s7 3 7 8z"/></svg></span>
      <span class="chip" style="width:45px">&#8804; 3</span>
      <span class="chip" style="width:45px">&gt; 3</span>
      <span class="chip" style="width:127px">All Limits <svg width="14" height="9" viewBox="0 0 14 9"><path d="M0 0h14L7 9z" fill="#111"/></svg></span>
    </div>
  </section>

  <section class="abs lobby" aria-label="Tables">
    <svg width="0" height="0" style="position:absolute">
      <defs>
        <linearGradient id="feltFill" x1="0" y1="0" x2="0" y2="1">
          <stop offset="0" stop-color="#0e2a08"/><stop offset=".6" stop-color="#3d7a1c"/><stop offset="1" stop-color="#c8e68a"/>
        </linearGradient>
        <symbol id="felt" viewBox="0 0 292 56">
          <polygon points="22,2 270,2 292,54 0,54" fill="url(#feltFill)" stroke="#fff" stroke-width="1.5"/>
          <line x1="11" y1="28" x2="281" y2="28" stroke="#fff" stroke-width="1.5"/>
          <g stroke="#fff" stroke-width="1.2">
            <line x1="57.4" y1="2" x2="41.7" y2="54"/><line x1="92.9" y1="2" x2="83.4" y2="54"/><line x1="128.3" y1="2" x2="125.1" y2="54"/>
            <line x1="163.7" y1="2" x2="166.9" y2="54"/><line x1="199.1" y1="2" x2="208.6" y2="54"/><line x1="234.6" y1="2" x2="250.3" y2="54"/>
          </g>
          <g font-family="Roboto,Arial,sans-serif" font-size="10" font-weight="700" font-style="italic" text-anchor="middle">
            <g fill="#ffe11a"><text x="37" y="20">B</text><text x="74" y="20">B</text><text x="110" y="20">B</text><text x="146" y="20">B</text><text x="182" y="20">B</text><text x="218" y="20">B</text><text x="255" y="20">B</text></g>
            <g fill="#fff"><text x="28" y="46">P</text><text x="68" y="46">P</text><text x="107" y="46">P</text><text x="146" y="46">P</text><text x="185" y="46">P</text><text x="224" y="46">P</text><text x="264" y="46">P</text></g>
          </g>
        </symbol>
        <symbol id="user" viewBox="0 0 20 18"><circle cx="10" cy="5" r="4.5" fill="#f5b25a"/><path d="M1 18c0-6 4-8 9-8s9 2 9 8z" fill="#f5b25a"/></symbol>
        <symbol id="down" viewBox="0 0 22 18"><path d="M7 1h8v7h6L11 17 1 8h6z" fill="#c98a10" stroke="#7a4a00"/></symbol>
      </defs>
    </svg>

    <article class="table-card" style="left:13px;top:15px">
      <span class="table-name">Baccarat A5-3C</span><span class="table-fee">Commission 0/7</span>
      <span class="table-limit">Bet Limit</span><span class="table-seats">0/100</span>
      <span class="join-coin">JOIN</span>
      <svg class="felt"><use href="#felt"/></svg>
      <div class="seat-row"><span class="seat"><svg width="20" height="18"><use href="#user"/></svg></span><span class="seat"><svg width="20" height="18"><use href="#user"/></svg></span><span class="seat"><svg width="20" height="18"><use href="#user"/></svg></span><span class="seat"><svg width="20" height="18"><use href="#user"/></svg></span><span class="seat"><svg width="20" height="18"><use href="#user"/></svg></span><span class="seat more"><svg width="22" height="18"><use href="#down"/></svg></span><span class="seat more"><svg width="22" height="18"><use href="#down"/></svg></span></div>
    </article>
    <article class="table-card" style="left:331px;top:15px">
      <span class="table-name">Baccarat A5-3C</span><span class="table-fee">Commission 0/7</span>
      <span class="table-limit">Bet Limit</span><span class="table-seats">0/100</span>
      <span class="join-coin">JOIN</span>
      <svg class="felt"><use href="#felt"/></svg>
      <div class="seat-row"><span class="seat"><svg width="20" height="18"><use href="#user"/></svg></span><span class="seat"><svg width="20" height="18"><use href="#user"/></svg></span><span class="seat"><svg width="20" height="18"><use href="#user"/></svg></span><span class="seat"><svg width="20" height="18"><use href="#user"/></svg></span><span class="seat"><svg width="20" height="18"><use href="#user"/></svg></span><span class="seat more"><svg width="22" height="18"><use href="#down"/></svg></span><span class="seat more"><svg width="22" height="18"><use href="#down"/></svg></span></div>
    </article>
    <article class="table-card" style="left:650px;top:15px">
      <span class="table-name">Baccarat A5-3C</span><span class="table-fee">Commission 0/7</span>
      <span class="table-limit">Bet Limit</span><span class="table-seats">0/100</span>
      <span class="join-coin">JOIN</span>
      <svg class="felt"><use href="#felt"/></svg>
      <div class="seat-row"><span class="seat"><svg width="20" height="18"><use href="#user"/></svg></span><span class="seat"><svg width="20" height="18"><use href="#user"/></svg></span><span class="seat"><svg width="20" height="18"><use href="#user"/></svg></span><span class="seat"><svg width="20" height="18"><use href="#user"/></svg></span><span class="seat"><svg width="20" height="18"><use href="#user"/></svg></span><span class="seat more"><svg width="22" height="18"><use href="#down"/></svg></span><span class="seat more"><svg width="22" height="18"><use href="#down"/></svg></span></div>
    </article>
    <article class="table-card" style="left:13px;top:178px">
      <span class="table-name">Baccarat A5-3C</span><span class="table-fee">Commission 0/7</span>
      <span class="table-limit">Bet Limit</span><span class="table-seats">0/100</span>
      <span class="join-coin">JOIN</span>
      <svg class="felt"><use href="#felt"/></svg>
      <div class="seat-row"><span class="seat"><svg width="20" height="18"><use href="#user"/></svg></span><span class="seat"><svg width="20" height="18"><use href="#user"/></svg></span><span class="seat"><svg width="20" height="18"><use href="#user"/></svg></span><span class="seat"><svg width="20" height="18"><use href="#user"/></svg></span><span class="seat"><svg width="20" height="18"><use href="#user"/></svg></span><span class="seat more"><svg width="22" height="18"><use href="#down"/></svg></span><span class="seat more"><svg width="22" height="18"><use href="#down"/></svg></span></div>
    </article>
    <article class="table-card" style="left:331px;top:178px">
      <span class="table-name">Baccarat A5-3C</span><span class="table-fee">Commission 0/7</span>
      <span class="table-limit">Bet Limit</span><span class="table-seats">0/100</span>
      <span class="join-coin">JOIN</span>
      <svg class="felt"><use href="#felt"/></svg>
      <div class="seat-row"><span class="seat"><svg width="20" height="18"><use href="#user"/></svg></span><span class="seat"><svg width="20" height="18"><use href="#user"/></svg></span><span class="seat"><svg width="20" height="18"><use href="#user"/></svg></span><span class="seat"><svg width="20" height="18"><use href="#user"/></svg></span><span class="seat"><svg width="20" height="18"><use href="#user"/></svg></span><span class="seat more"><svg width="22" height="18"><use href="#down"/></svg></span><span class="seat more"><svg width="22" height="18"><use href="#down"/></svg></span></div>
    </article>
    <article class="table-card" style="left:650px;top:178px">
      <span class="table-name">Baccarat A5-3C</span><span class="table-fee">Commission 0/7</span>
      <span class="table-limit">Bet Limit</span><span class="table-seats">0/100</span>
      <span class="join-coin">JOIN</span>
      <svg class="felt"><use href="#felt"/></svg>
      <div class="seat-row"><span class="seat"><svg width="20" height="18"><use href="#user"/></svg></span><span class="seat"><svg width="20" height="18"><use href="#user"/></svg></span><span class="seat"><svg width="20" height="18"><use href="#user"/></svg></span><span class="seat"><svg width="20" height="18"><use href="#user"/></svg></span><span class="seat"><svg width="20" height="18"><use href="#user"/></svg></span><span class="seat more"><svg width="22" height="18"><use href="#down"/></svg></span><span class="seat more"><svg width="22" height="18"><use href="#down"/></svg></span></div>
    </article>

    <div class="abs scroll-track"><div class="abs scroll-thumb"></div></div>
  </section>

  <footer class="abs bottom-bar"></footer>
  <div class="abs balance">
    <span class="balance-label">Balance</span>
    <span class="currency">$ SGD &#9664;</span>
    <span class="balance-value">999,999,999</span>
    <span class="balance-end"></span>
  </div>

</main>
</body>
</html>
```